EILT: Landing Page - EXPRESS VERSAND
Zielgruppe
Es soll in kurzer Zeit (max 48 Stunden) eine kleine Ladingpage entstehen. Expressversand / Import von China nach Deutschland . Aufgrund der stark steigenden Luftfrachtraten aus China heraus hat sich unsere Firma Fracht-Kapazitäten gesichert. Diese sollen nun angeboten werden. Über eine Ladingpage sollen Anfragen generiert werden. Diese Anfragen werden dann mit einem Angebot von uns beantwortet. Expressversand / Import von China nach Deutschland
Aufgabenstellung
Die Seite soll beinhalten:
- 1-2 Bilder (z. B. Luftfracht, Logistik, Flugzeug, Cargo, etc)
- kurzer erklärender Text: z.B. 'jetzt Angebot anfordern und günstig aus China per Express versenden.' Inkl. Abholung, Verzollung und Zustellung. Kurze Laufzeit von nur 3-5 Tagen. ab 45€ / Paket
- Anfrage Formular, bestehend aus: , Abholadresse in China/Post Code, ZielAdresse Deutschland, Sendungsinformationen (wie viele Kartons, wie schwer ist ein Karton und welche Abmessungen L/B/H ), wann ist die Sendung in China abholbereit, optional: Sendungsinhalt (Ware, Zolltarifnummer/HS Code) , Firma, Name, email adresse
- optional ein Header/Laufband etc mit: Bis zum 19. Nov 21 versenden - Ware bis MegaSonntag erhalten!
- 24h Servicehotline, Tel: 0987/314265
- 2-3 Kundenreferenzen: Bilder von Personen mit Text : „Schneller Versand - nur 4 Tage Laufzeit“ , „1A Service, ohne Probleme“ , „gute Preise - nur zu empfehlen.“
Unser Firmenlogo kann - muss aber nicht auftauchen.
In der farblichen Gestaltung haben Sie freie Hand und freuen uns auf Ihre Vorschläge.
Aufgrund der Dringlichkeit sollte diese Landingpage innerhalb 48 Stunden 'live ' gehen.
WICHTIG: Die Page sollte von Ihnen auch veröffentlich werden. Aktuell nutzen wir den Kelvo Homepagebaukasten. Die Page kann aber auch durch andere Anbieter veröffentlicht werden , zb Pagerune

```html
<!DOCTYPE html>
<html lang="de">
<head>
<meta charset="utf-8">
<title>Expressversand China – Deutschland</title>
<link rel="stylesheet" href="https://fonts.googleapis.com/css2?family=PT+Sans:wght@400;700&display=swap">
<style>
  :root {
    --bg: #04293a;
    --bg-deep: #03212d;
    --card: #1b3d4a;
    --accent: #fbca5a;
    --accent-soft: rgba(251, 202, 90, 0.14);
    --field-line: #2e9ad6;
    --text: #ffffff;
    --quote: #1c4150;
    --rule: #2a4a56;
  }
  * { margin: 0; padding: 0; box-sizing: border-box; }
  html, body { width: 1200px; height: 1116px; overflow: hidden; }
  body {
    background: var(--bg);
    color: var(--text);
    font-family: "PT Sans", "Myriad Pro", sans-serif;
    position: relative;
  }
  .brand {
    position: absolute; left: 154px; top: 30px;
    display: flex; align-items: center; gap: 8px;
  }
  .brand-dot { width: 40px; height: 40px; border-radius: 50%; background: var(--accent); }
  .brand-name { font-size: 34px; font-weight: 700; color: var(--text); }
  .headline {
    position: absolute; left: 150px; top: 131px;
    font-size: 55px; line-height: 53px; font-weight: 700; color: var(--accent);
  }
  .hotline { position: absolute; left: 149px; top: 330px; }
  .hotline-label { font-size: 25px; font-weight: 700; }
  .hotline-number { font-size: 37px; font-weight: 700; line-height: 42px; letter-spacing: 0.5px; }
  .hero-photo {
    position: absolute; left: 598px; top: 25px; width: 460px; height: 427px;
    background: #fff; padding: 16px;
  }
  .hero-photo-fill {
    width: 100%; height: 100%;
    background: linear-gradient(120deg, #0d4a5a 0%, #0a3a48 55%, #7a4030 80%, #3a4a55 100%);
  }
  .pointer-art {
    position: absolute; left: 128px; top: 499px; width: 52px; height: 146px;
    border-radius: 26px; background: var(--accent-soft);
  }
  .intro {
    position: absolute; left: 150px; width: 900px; top: 508px;
    text-align: center; font-size: 22px; line-height: 32px; font-weight: 700;
  }
  .intro em { font-style: normal; color: var(--accent); }
  .request-form {
    position: absolute; left: 202px; top: 601px; width: 797px;
    display: grid; grid-template-columns: 249px 249px 249px; column-gap: 25px; row-gap: 16px;
  }
  .field {
    height: 40px; border: 2px solid var(--field-line); border-radius: 4px;
    background: var(--bg-deep); color: var(--text);
    font: 400 13px "PT Sans", sans-serif; padding: 0 15px;
  }
  .field::placeholder { color: var(--text); opacity: 1; }
  .field-wide { grid-column: 1 / -1; }
  .submit {
    position: absolute; left: 477px; top: 826px; width: 250px; height: 41px;
    background: var(--accent); border: none; border-radius: 3px;
    display: flex; align-items: center; justify-content: center; gap: 10px;
    font: 700 17px "PT Sans", sans-serif; color: var(--bg-deep);
  }
  .quote-mark {
    position: absolute; left: 146px; top: 806px;
    font-size: 200px; line-height: 1; font-weight: 700; color: var(--quote);
    font-family: "PT Sans", sans-serif;
  }
  .testimonial {
    position: absolute; top: 901px; width: 289px; height: 126px;
    background: var(--card); border-radius: 3px; text-align: center;
  }
  .testimonial-quote { margin-top: 16px; font-size: 15px; }
  .testimonial-author {
    display: flex; align-items: center; justify-content: center; gap: 8px; margin-top: 14px;
  }
  .avatar { width: 54px; height: 54px; border-radius: 50%; background: linear-gradient(160deg, #8a5a44, #3a2a24); }
  .author-info { text-align: left; }
  .author-name { font-size: 13px; }
  .stars { color: var(--accent); font-size: 13px; letter-spacing: 0; }
  .footer-rule { position: absolute; left: 154px; top: 1069px; width: 898px; height: 1px; background: var(--rule); }
  .copyright { position: absolute; top: 1083px; width: 1200px; text-align: center; font-size: 13px; }
</style>
</head>
<body>
  <div class="brand">
    <span class="brand-dot"></span>
    <span class="brand-name">KVR</span>
  </div>

  <h1 class="headline">Expressversand /<br>Import von China<br>nach Deutschland</h1>

  <div class="hotline">
    <div class="hotline-label">24h Servicehotline</div>
    <div class="hotline-number">Tel: 0987/314265</div>
  </div>

  <div class="hero-photo">
    <div class="hero-photo-fill" role="img" aria-label="Luftaufnahme eines Frachtflugzeugs über einem Containerschiff und Hafen"></div>
  </div>

  <div class="pointer-art" role="img" aria-label="Geschwungener, handgezeichneter Pfeil, der auf das Formular zeigt"></div>

  <p class="intro">Jetzt Angebot anfordern und günstig aus China per Express versenden.' Inkl. Abholung,<br>Verzollung und Zustellung. Kurze Laufzeit von nur <em>3-5 Tagen</em>. ab <em>45€ / Paket</em></p>

  <form class="request-form">
    <input class="field" type="text" placeholder="Firma">
    <input class="field" type="text" placeholder="Name">
    <input class="field" type="email" placeholder="Email Adresse">
    <input class="field" type="text" placeholder="Abholadresse in China">
    <input class="field" type="text" placeholder="Post Code">
    <input class="field" type="text" placeholder="ZielAdresse Deutschland">
    <input class="field" type="text" placeholder="Wie Viele Kartons">
    <input class="field" type="text" placeholder="Karton Gewicht">
    <input class="field" type="text" placeholder="Abmessungen  L / W / H">
    <input class="field field-wide" type="text" placeholder="Abholbereit in China ab (Datum)">
  </form>

  <button class="submit" type="submit">
    <svg width="18" height="18" viewBox="0 0 18 18" fill="none" stroke="#03212d" stroke-width="1.4" stroke-linejoin="round">
      <path d="M1 10 L17 1 L12 17 L9 11 Z"/><path d="M9 11 L17 1"/><path d="M5 13 L5 17 L8 14"/>
    </svg>
    SENDEN
  </button>

  <div class="quote-mark" aria-hidden="true">“</div>

  <div class="testimonial" style="left:153px">
    <p class="testimonial-quote">Schneller Versand - nur 4 Tage Laufzeit</p>
    <div class="testimonial-author">
      <div class="avatar" role="img" aria-label="Porträtfoto eines Kunden"></div>
      <div class="author-info"><div class="author-name">Ravel Tomsen</div><div class="stars">★★★★★</div></div>
    </div>
  </div>

  <div class="testimonial" style="left:456px">
    <p class="testimonial-quote">1A Service, ohne Probleme</p>
    <div class="testimonial-author">
      <div class="avatar" role="img" aria-label="Porträtfoto eines Kunden"></div>
      <div class="author-info"><div class="author-name">Jorin Malek</div><div class="stars">★★★★★</div></div>
    </div>
  </div>

  <div class="testimonial" style="left:759px">
    <p class="testimonial-quote">Gute Preise - nur zu empfehlen.</p>
    <div class="testimonial-author">
      <div class="avatar" role="img" aria-label="Porträtfoto eines Kunden"></div>
      <div class="author-info"><div class="author-name">Ravel Tomsen</div><div class="stars">★★★★★</div></div>
    </div>
  </div>

  <div class="footer-rule"></div>
  <p class="copyright">Copyright 2021. Alle Rechte vorbehalten.</p>
</body>
</html>
```